Sri Lankan Cricket Tour For Girls Aged 14-18 in July 2018

We need a flyer to promote a cricket tour of Sri Lanka in July 2018 for girls aged 14-18.
We want the flyer to call for "expressions of interest".
We would like the Sri Lankan Flag also images of cricket ball and beaches and palm trees etc.
Mention Level 3 Coaches with International experience.
Target market is parents of girls aged 14 to 18 and girls aged 14 to 18

Target Market(s)

Parents of girls aged 14 to 18 and girls aged 14 to 18

Industry/Entity Type

Travel

Font styles to use
Serif
Sans Serif

Colors
0355a3
ec1f27
fbed22

Requirements
Must have
• Sri Lankan Flag, Halvey Athletics Logo, email address boyd@halveyathletics.com.au.
• - 10 Day Tour
• - Play on First Class Grounds
• - Level 3 Coaches With International Experience
• - For More Information Contact Boyd boyd@halveyathletics.com.au
Nice to have
• Picture of girls playing cricket, sun and beach
Should not have
• Cartoon type images
• Photo's of actual cricketers

```html
<!DOCTYPE html>
<html lang="en">
<head>
<meta charset="utf-8">
<title>Cricket Tour of Sri Lanka for Girls – Halvey Athletics</title>
<link rel="stylesheet" href="https://fonts.googleapis.com/css2?family=Oswald:wght@400;500;600;700&display=swap">
<style>
  :root {
    --navy: #0a1d38;
    --blue: #0355a3;
    --red: #ec1f27;
    --yellow: #fbed22;
    --white: #ffffff;
    --sea: #2f8e9c;
    --sand: #d9d2c0;
    --flag-gold: #f5b41d;
    --flag-maroon: #8d1b2b;
    --flag-green: #00804a;
    --flag-orange: #ea7224;
  }
  * { margin: 0; padding: 0; box-sizing: border-box; }
  html, body { width: 793px; height: 1200px; overflow: hidden; background: var(--navy); }
  .flyer {
    position: relative;
    width: 793px; height: 1200px;
    overflow: hidden;
    font-family: "Oswald", "Arial Narrow", sans-serif;
    color: var(--white);
    text-transform: uppercase;
  }
  .scene {
    position: absolute; inset: 0;
    background:
      radial-gradient(ellipse 60% 45% at 50% 48%, rgba(236,120,40,.75), rgba(236,31,39,.25) 45%, rgba(0,0,0,0) 75%),
      linear-gradient(180deg, #0c2140 0%, #1d3556 22%, #5a6a6c 42%, #8a7f52 55%, #4f8e8a 72%, var(--sea) 82%, var(--sand) 100%);
  }
  .duration { position: absolute; left: 38px; top: 22px; text-align: center; line-height: 1; font-weight: 700; }
  .duration-number { font-size: 64px; display: block; }
  .duration-label { font-size: 34px; letter-spacing: 2px; display: block; margin-top: 4px; }
  .brand { position: absolute; left: 0; right: 0; top: 22px; text-align: center; }
  .brand-mark {
    width: 142px; height: 142px; border-radius: 50%;
    background: var(--white); margin: 0 auto;
  }
  .brand-name {
    margin-top: 12px; font-size: 34px; font-weight: 600;
    letter-spacing: 3px; color: var(--blue);
  }
  .flag { position: absolute; left: 620px; top: 63px; width: 108px; height: 66px; }
  .headline {
    position: absolute; left: 0; right: 0; top: 515px;
    text-align: center; font-weight: 700; font-size: 104px; line-height: .9;
    color: var(--red);
    -webkit-text-stroke: 3px var(--white);
    paint-order: stroke fill;
    text-shadow: 0 4px 10px rgba(0,0,0,.45);
  }
  .headline-accent { color: var(--yellow); }
  .side-note {
    position: absolute; top: 862px; font-size: 17px; font-weight: 500;
    letter-spacing: 7px; line-height: 1.45; text-align: center;
  }
  .side-note--left { left: 28px; width: 190px; }
  .side-note--right { right: 28px; width: 130px; }
  .age { position: absolute; left: 0; right: 0; top: 845px; text-align: center; font-size: 56px; font-weight: 700; }
  .date { position: absolute; left: 0; right: 0; top: 935px; text-align: center; font-size: 38px; font-weight: 500; letter-spacing: 8px; color: var(--yellow); }
  .coaches { position: absolute; left: 0; right: 0; top: 1005px; text-align: center; font-size: 27px; font-weight: 500; letter-spacing: 2px; }
  .contact {
    position: absolute; left: 0; right: 0; bottom: 0; height: 135px;
    background: var(--red); text-align: center; padding-top: 16px;
  }
  .contact-label { font-size: 27px; font-weight: 600; text-transform: none; letter-spacing: 1px; }
  .contact-email { font-size: 40px; font-weight: 500; text-transform: none; letter-spacing: 5px; margin-top: 4px; display: block; }
</style>
</head>
<body>
<main class="flyer">
  <div class="scene" role="img" aria-label="Girl cricketer in helmet swinging a bat, cricket ball in flight, cloudy sky and tropical beach with sea"></div>

  <div class="duration">
    <span class="duration-number">10</span>
    <span class="duration-label">Day Tour</span>
  </div>

  <div class="brand">
    <div class="brand-mark"></div>
    <div class="brand-name">Halvey Athletics</div>
  </div>

  <svg class="flag" viewBox="0 0 108 66" aria-label="Flag of Sri Lanka" role="img">
    <rect width="108" height="66" fill="var(--flag-gold)"/>
    <rect x="5" y="5" width="13" height="56" fill="var(--flag-green)"/>
    <rect x="19" y="5" width="13" height="56" fill="var(--flag-orange)"/>
    <rect x="36" y="5" width="67" height="56" fill="var(--flag-maroon)"/>
  </svg>

  <h1 class="headline">Cricket Tour<br>of <span class="headline-accent">Sri Lanka</span><br>for Girls</h1>

  <p class="side-note side-note--left">Expressions<br>of<br>Interest</p>
  <p class="age">Aged 14-18</p>
  <p class="side-note side-note--right">First<br>Class<br>Grounds</p>

  <p class="date">July 2018</p>
  <p class="coaches">Level 3 Coaches with International Experience</p>

  <footer class="contact">
    <p class="contact-label">For More Information Contact</p>
    <span class="contact-email">boyd@halveyathletics.com.au</span>
  </footer>
</main>
</body>
</html>
```